Hydrographic business needs a business card that reaches hunters and off-road enthusiasts

We need a business card for a new hydrographics company catering to customers such as hunters, off-road ATV riders and custom vehicle enthusiasts. A western theme is preferred but professional. Our service should be thought of as upper end graphic design on firearms, off road vehicles, motorcycles, etc... See www.dellowfx.com for ideas on patterns, colors, etc...

Target Market(s)

Hunters, off road enthusiasts, custom car enthusiasts, motorcycle riders...

Industry/Entity Type

Graphic Design

```html
<!DOCTYPE html>
<html lang="en">
<head>
<meta charset="utf-8">
<title>Dellow Hydro Graphics – Business Card</title>
<link href="https://fonts.googleapis.com/css2?family=Questrial&family=Montserrat:wght@700&display=swap" rel="stylesheet">
<style>
  :root {
    --bg: #4a4a4a;
    --card: #2a2627;
    --card-back: #2b2829;
    --tab: #1f1c1d;
    --orange: #f6a11a;
    --yellow: #ffd000;
    --deep-orange: #f28c1c;
    --light: #d9d6d3;
    --muted: #a9a5a2;
  }
  * { margin: 0; padding: 0; box-sizing: border-box; }
  html, body { width: 1200px; height: 799px; overflow: hidden; }
  body {
    background: var(--bg);
    position: relative;
    font-family: "Questrial", sans-serif;
  }
  .card {
    position: absolute;
    top: 251px;
    width: 520px;
    height: 297px;
    border-radius: 22px;
    overflow: hidden;
    box-shadow: 0 10px 24px rgba(0,0,0,.45);
  }
  .card--front { left: 50px; background: var(--card); }
  .card--back  { left: 630px; background: var(--card-back); }

  .front__swoosh { position: absolute; left: 0; top: 0; width: 520px; height: 297px; }
  .front__company {
    position: absolute; left: 150px; top: 44px;
    color: var(--orange); font-size: 30px; letter-spacing: .2px;
  }
  .front__name {
    position: absolute; left: 40px; top: 124px;
    color: var(--muted); font-size: 27px;
  }
  .front__divider {
    position: absolute; left: 206px; top: 118px;
    width: 2px; height: 56px; background: var(--orange);
  }
  .front__contacts {
    position: absolute; left: 222px; top: 108px;
    list-style: none;
  }
  .front__contacts li {
    display: flex; align-items: center; gap: 7px;
    color: var(--light); font-size: 15px; line-height: 17px;
  }
  .front__contacts svg { width: 11px; height: 11px; flex: none; }

  .back__tab {
    position: absolute; left: 0; top: 40px;
    padding: 12px 26px 12px 22px;
    background: var(--tab);
    border-radius: 0 26px 26px 0;
    color: var(--orange);
    font-family: "Montserrat", sans-serif; font-weight: 700; font-size: 17px;
  }
  .back__mark {
    position: absolute; left: 0; right: 0; top: 128px;
    display: flex; justify-content: center; align-items: center; gap: 10px;
  }
  .back__mark-square { width: 14px; height: 14px; background: var(--orange); }
  .back__mark-name {
    color: var(--orange);
    font-family: "Montserrat", sans-serif; font-weight: 700; font-size: 40px;
  }
  .back__tagline {
    position: absolute; left: 0; right: 0; top: 236px;
    text-align: center; color: var(--light); font-size: 13px;
  }
</style>
</head>
<body>
  <section class="card card--front" aria-label="Card front">
    <svg class="front__swoosh" viewBox="0 0 520 297" aria-hidden="true">
      <defs>
        <linearGradient id="swooshGrad" x1="0" y1="1" x2="1" y2="0">
          <stop offset="0" stop-color="var(--yellow)"/>
          <stop offset="1" stop-color="var(--orange)"/>
        </linearGradient>
      </defs>
      <path d="M250 297 C380 280 470 240 520 150 L520 297 Z" fill="url(#swooshGrad)"/>
      <path d="M400 297 C450 285 495 255 520 215 L520 297 Z" fill="var(--deep-orange)"/>
    </svg>
    <div class="front__company">Dellow Hydro Graphics</div>
    <div class="front__name">Wade Dellow</div>
    <div class="front__divider"></div>
    <ul class="front__contacts">
      <li><svg viewBox="0 0 12 12"><circle cx="6" cy="6" r="5" fill="none" stroke="var(--orange)" stroke-width="1.3"/><path d="M4 3.5 L5 5 L4.5 6 Q5.5 7.5 6 7.5 L7 7 L8.5 8" fill="none" stroke="var(--orange)" stroke-width="1"/></svg>555-201-7788</li>
      <li><svg viewBox="0 0 12 12"><circle cx="6" cy="6" r="5" fill="none" stroke="var(--orange)" stroke-width="1.3"/><circle cx="6" cy="5" r="1.5" fill="var(--orange)"/></svg>112 Mesa Ridge Road 2040</li>
      <li><svg viewBox="0 0 12 12"><circle cx="6" cy="6" r="5" fill="none" stroke="var(--orange)" stroke-width="1.3"/><circle cx="6" cy="5" r="1.5" fill="var(--orange)"/></svg>Cedar Flat, TX 75001</li>
      <li><svg viewBox="0 0 12 12"><circle cx="6" cy="6" r="5" fill="none" stroke="var(--orange)" stroke-width="1.3"/><path d="M2 6 H10 M6 2 V10" stroke="var(--orange)" stroke-width="1"/></svg>www.dellowfx.com</li>
      <li><svg viewBox="0 0 12 12"><circle cx="6" cy="6" r="5" fill="none" stroke="var(--orange)" stroke-width="1.3"/><rect x="3.5" y="4.2" width="5" height="3.6" fill="none" stroke="var(--orange)" stroke-width="1"/></svg>wade@dellowfx.com</li>
    </ul>
  </section>

  <section class="card card--back" aria-label="Card back">
    <div class="back__tab">Dellow Hydro Graphics</div>
    <div class="back__mark">
      <span class="back__mark-square"></span>
      <span class="back__mark-name">DELLOW</span>
    </div>
    <p class="back__tagline">The best and most reliable hydrographics service in Texas</p>
  </section>
</body>
</html>
```